Mailout - IT sales/service - DL sized

Long standing local computer store in central Melbourne that is very customer focussed. Wide range of products and services for medium enterprise, small/medium business & home/students.

Want to get the word out there to let people know we are here as most don't know hence a mailout (DL sized double-sided).

The image we want to portray is NOT of:
- one-man driving around in his own support business who will fix something and not come back if there is an issue
- your everyday corner computer store who have young sales staff with not much "out-in-the-field" experience
- cheap & nasty service

The image we DO want to portay is:
- Professional service at a reasonable price
- responsible sales/technical support team that have a bricks & mortar store
- trustworthy & friendly business
- wide range of services from new office setups, inhouse/onsite/remote support capabilities, procurement, consultation for PC & Mac
- Customer service quality (a previous finalist in the Crestfield Enterprise Medals for Customer Service) voted by customers
- We sell and service although this leaflet is biased towards the service side

Our immediate location/area is full of small/medium business and students/home users as we are next to the CBD with Universities, apartments and townhouses, cafes.

I have attached a leaflet that we did inhouse and was in the middle of editing until i found Makerhive. My skills are very basic as you can see and thought it could be much better! I'll stick to service/sales thanks =)

Target Market(s)

Small/Medium business, home/student users. First distribution to local then if successful, surrounding areas

Industry/Entity Type

Computer

Requirements
Must have
• Our logo file is attached. Our company name has a specific font called Prototype.
The PC&Mac sign (i just did that in Illustrator).
The 2 offers - my call to action! (obviously needs to be editcable)
File will need to be ready for print at the printing shops.
Nice to have
• A nice blue with black and white is good. then another colour say a suitbale red or orange for anything that needs to stand out perhaps.
I've attached 3 pictures. Hopefully 1 of them can be used to depict the service side.
A map of our location as our street gets cut into sections but you can't drive right through them all.
Usage of one pic whether it is one of the ones provided or if you have a more suitable one.

```html
<!DOCTYPE html>
<html lang="en">
<head>
<meta charset="utf-8">
<title>Kestrel Computers – DL Mailout</title>
<link rel="stylesheet" href="https://fonts.googleapis.com/css2?family=Alfa+Slab+One&family=Noto+Serif:wght@400;700&display=swap">
<style>
  :root {
    --sky: #1fb6ee;
    --sky-pale: #dff1fb;
    --orange: #f7874a;
    --ink: #1c1c1c;
    --paper: #ffffff;
    --backdrop: #e6e6e6;
    --slab: "Alfa Slab One", "Rockwell", serif;
    --body: "Noto Serif", Georgia, serif;
  }
  * { box-sizing: border-box; margin: 0; padding: 0; }
  html, body { width: 1200px; height: 800px; overflow: hidden; }
  body {
    background: var(--backdrop);
    font-family: var(--body);
    color: var(--ink);
    display: flex;
    flex-direction: column;
    align-items: center;
    justify-content: center;
    gap: 20px;
  }
  .dl-card {
    position: relative;
    width: 780px;
    height: 368px;
    background: var(--paper);
    overflow: hidden;
    box-shadow: 0 2px 6px rgba(0,0,0,.15);
  }

  /* ---------- Front ---------- */
  .front__panel {
    position: absolute;
    inset: 0;
    background: var(--sky);
    clip-path: polygon(0 0, 56% 0, 36% 100%, 0 100%);
  }
  .front__question {
    position: absolute;
    left: 34px;
    top: 26px;
    font-family: var(--slab);
    color: var(--paper);
    text-transform: uppercase;
    line-height: 0.95;
  }
  .front__question-line { display: block; font-size: 50px; letter-spacing: 1px; }
  .front__question-mark { display: block; font-size: 150px; margin-left: 60px; line-height: 1.05; }
  .front__pitch {
    position: absolute;
    left: 450px;
    top: 56px;
    font-family: var(--slab);
    text-transform: uppercase;
    line-height: 1.02;
  }
  .pitch__line { display: block; font-size: 26px; color: var(--sky); white-space: nowrap; }
  .pitch__line--accent { color: var(--orange); }
  .pitch__line--big { display: block; font-size: 54px; color: var(--orange); line-height: 1; }
  .front__illustration {
    position: absolute;
    right: 34px;
    bottom: 16px;
    width: 130px;
    height: 88px;
    border-radius: 8px;
    background: linear-gradient(160deg, #f1f1f1, #cfd3d6);
  }

  /* ---------- Back ---------- */
  .back { display: grid; grid-template-columns: 1.05fr 1fr 0.8fr; }
  .back__column { padding: 24px 22px; }
  .feature { margin-bottom: 18px; }
  .feature__title {
    display: flex;
    align-items: center;
    gap: 6px;
    font-family: var(--slab);
    color: var(--sky);
    text-transform: uppercase;
    font-size: 20px;
    line-height: 1;
    margin-bottom: 8px;
  }
  .feature__text { font-size: 11.5px; line-height: 1.45; color: var(--sky); }
  .back__note { font-size: 11px; line-height: 1.45; color: var(--orange); }
  .offers { display: flex; flex-direction: column; gap: 12px; padding: 18px 14px; }
  .offer {
    background: var(--sky-pale);
    padding: 16px 16px 14px;
    flex: 1;
  }
  .offer__title {
    font-family: var(--slab);
    color: var(--sky);
    text-transform: uppercase;
    font-size: 26px;
    line-height: 0.95;
    margin-bottom: 8px;
  }
  .offer__deal { font-size: 19px; color: var(--orange); margin-bottom: 4px; }
  .offer__detail { font-size: 12px; line-height: 1.4; color: var(--ink); }
  .brand {
    display: flex;
    flex-direction: column;
    align-items: center;
    justify-content: center;
    gap: 16px;
    height: 100%;
  }
  .brand__mark { width: 78px; height: 78px; border-radius: 50%; background: var(--sky); }
  .brand__name { font-family: var(--body); font-weight: 700; font-size: 17px; color: var(--ink); white-space: nowrap; }
  .contact { display: flex; align-items: center; gap: 8px; font-size: 13px; color: var(--ink); }
</style>
</head>
<body>

  <section class="dl-card front" aria-label="Mailout front">
    <div class="front__panel"></div>
    <h1 class="front__question">
      <span class="front__question-line">Computer</span>
      <span class="front__question-line">Problems</span>
      <span class="front__question-mark">?</span>
    </h1>
    <p class="front__pitch">
      <span class="pitch__line">We can help</span>
      <span class="pitch__line pitch__line--accent">Professional</span>
      <span class="pitch__line">Easy to follow</span>
      <span class="pitch__line">Tech support</span>
      <span class="pitch__line">Really does</span>
      <span class="pitch__line--big">Exist</span>
    </p>
    <div class="front__illustration" role="img" aria-label="Illustration of a tech support figure with a megaphone, first aid kit and computer tower"></div>
  </section>

  <section class="dl-card back" aria-label="Mailout back">
    <div class="back__column">
      <div class="feature">
        <h2 class="feature__title">
          <svg width="20" height="16" viewBox="0 0 20 16" aria-hidden="true"><path d="M0 0h6l8 8-8 8H0l8-8zM8 0h4l8 8-8 8H8l8-8z" fill="var(--sky)"/></svg>
          Stress free
        </h2>
        <p class="feature__text">No jargon, no surprises. Our friendly in-store team explains every fix in plain words and quotes before any work begins.</p>
      </div>
      <div class="feature">
        <h2 class="feature__title">
          <svg width="20" height="16" viewBox="0 0 20 16" aria-hidden="true"><path d="M0 0h6l8 8-8 8H0l8-8zM8 0h4l8 8-8 8H8l8-8z" fill="var(--sky)"/></svg>
          Flexible service
        </h2>
        <p class="feature__text">In store, on site or remote, we support PC and Mac for homes, students and growing offices across the city.</p>
      </div>
      <p class="back__note">Offers valid until 30 June. Mention this card when booking.</p>
    </div>

    <div class="offers">
      <article class="offer">
        <h3 class="offer__title">Business<br>Offer</h3>
        <p class="offer__deal">Free 1 hr IT audit.</p>
        <p class="offer__detail">See how we can get technology working better for you.</p>
      </article>
      <article class="offer">
        <h3 class="offer__title">Home/Student<br>Offer</h3>
        <p class="offer__deal">20% off Service</p>
        <p class="offer__detail">Get 20% off the labour cost of your service.</p>
      </article>
    </div>

    <div class="back__column">
      <div class="brand">
        <div class="brand__mark" aria-hidden="true"></div>
        <p class="brand__name">Kestrel Computers</p>
        <p class="contact">
          <svg width="16" height="16" viewBox="0 0 24 24" aria-hidden="true"><path d="M6.6 10.8a15.1 15.1 0 0 0 6.6 6.6l2.2-2.2a1 1 0 0 1 1-.25 11.4 11.4 0 0 0 3.6.57 1 1 0 0 1 1 1V20a1 1 0 0 1-1 1A17 17 0 0 1 3 4a1 1 0 0 1 1-1h3.5a1 1 0 0 1 1 1c0 1.25.2 2.45.57 3.57a1 1 0 0 1-.25 1z" fill="var(--sky)"/></svg>
          (03) 9000 4127
        </p>
      </div>
    </div>
  </section>

</body>
</html>
```